Business Card Design Project

I need a business card for an environmentally friendly interior design company called Maplecrest Decor.
I was thinking it might be nice to print the business cards on brown recycled paper with green ink.
In addition to interior design, I will also be able to consult with homeowners regarding their indoor environments and how they might be affecting their health after May 2013 which is when I will complete my certification program. This can be added to the business card at that time: "Certified Dwelling Vitality Environmental Consultant".

```html
<!DOCTYPE html>
<html lang="en">
<head>
<meta charset="utf-8">
<title>Maplecrest Decor – Business Card</title>
<link rel="stylesheet" href="https://fonts.googleapis.com/css2?family=Quicksand:wght@400;500;600;700&display=swap">
<style>
  :root {
    --page: #ffffff;
    --paper-light: #ddd8cf;
    --paper-mid: #d2ccc1;
    --paper-dark: #c9c2b6;
    --ink-deep: #2c5428;
    --ink-leaf: #4a7a3c;
    --ink-sage: #5a7150;
  }
  html, body {
    margin: 0;
    padding: 0;
    width: 1200px;
    height: 900px;
    overflow: hidden;
    background: var(--page);
  }
  .canvas {
    position: relative;
    width: 1200px;
    height: 900px;
    background: var(--page);
    font-family: "Quicksand", sans-serif;
  }
  .card {
    position: absolute;
    left: 190px;
    top: 216px;
    width: 820px;
    height: 354px;
  }
  .card-paper {
    position: absolute;
    inset: 0;
    width: 100%;
    height: 100%;
    display: block;
  }
  .card-text {
    position: absolute;
    left: 56px;
    margin: 0;
    line-height: 1;
    white-space: nowrap;
  }
  .brand-name {
    top: 50px;
    font-size: 46px;
    font-weight: 500;
    letter-spacing: 0.2em;
    text-transform: uppercase;
    color: var(--ink-deep);
  }
  .tagline {
    top: 112px;
    font-size: 29px;
    font-weight: 500;
    color: var(--ink-leaf);
  }
  .contact {
    top: 201px;
    font-size: 27px;
    font-weight: 700;
    color: var(--ink-deep);
    word-spacing: 0.08em;
  }
  .contact-phone {
    margin-left: 14px;
  }
  .credential {
    top: 253px;
    font-size: 24.5px;
    font-weight: 500;
    color: var(--ink-sage);
  }
</style>
</head>
<body>
  <main class="canvas">
    <section class="card">
      <svg class="card-paper" viewBox="0 0 820 354" role="img" aria-label="Recycled handmade paper texture with scattered plant fibers and small purple flecks">
        <defs>
          <linearGradient id="paper-tone" x1="0" y1="0" x2="1" y2="1">
            <stop offset="0" stop-color="var(--paper-light)"/>
            <stop offset="0.55" stop-color="var(--paper-mid)"/>
            <stop offset="1" stop-color="var(--paper-dark)"/>
          </linearGradient>
        </defs>
        <rect width="820" height="354" fill="url(#paper-tone)"/>
      </svg>
      <h1 class="card-text brand-name">Maplecrest Decor</h1>
      <p class="card-text tagline">environmentally friendly design</p>
      <p class="card-text contact"><span class="contact-name">Laurel Ann Briggs</span><span class="contact-phone">713.555.0142</span></p>
      <p class="card-text credential">Certified Dwelling Vitality Environmental Consultant</p>
    </section>
  </main>
</body>
</html>
```